Branded Resources for ORBALQa--Word, PPT, Newsletter Templates

Hi,
I hope you are well. I am hoping to get some pricing on branding a Word and PPT template and a Newsletter template. I've uploaded the original files for quick reference.

I was hoping for a full-color version and a black/grayscale version of the word and PPT template. Full color for the newsletter.

Thanks in advance for your quote and expected timeline for this project.

Thanks,
Velisse
Updates

Thank you for your submission and patience. I had a family emergency, and just getting back online. I will review the submissions. Thank you. Velisse

Industry/Entity Type

management consulting. Here's my website: https://orbalqa.example/

Requirements
Must have
• The Word, PPT and Newsletter templates should reflect the logo assets listed below. Open to complementary colors that complement red/orange/golds
Nice to have
• Vibrancy, diversity, community

```html
<!DOCTYPE html>
<html lang="en">
<head>
<meta charset="utf-8">
<title>ORBALQa Newsletter Template</title>
<link href="https://fonts.googleapis.com/css2?family=Montserrat:wght@400;600;700&family=Roboto+Condensed:wght@700&display=swap" rel="stylesheet">
<style>
  :root {
    --backdrop: #a0a1a3;
    --paper: #ffffff;
    --brand-red: #72241f;
    --ink: #3d3d3d;
    --heading-ink: #333333;
    --footer-band: #000000;
    --mark-gold: #b8742a;
    --name-ink: #222222;
    --label-white: #ffffff;
  }
  * { box-sizing: border-box; margin: 0; padding: 0; }
  html, body { width: 1200px; height: 960px; overflow: hidden; }
  body {
    position: relative;
    background: var(--backdrop);
    font-family: "Montserrat", Arial, sans-serif;
    color: var(--ink);
  }
  .sheet-label {
    position: absolute;
    right: 62px;
    top: 62px;
    font-family: Arial, Helvetica, sans-serif;
    font-size: 20px;
    color: var(--label-white);
    letter-spacing: 0.2px;
  }
  .page {
    position: absolute;
    top: 145px;
    width: 518px;
    height: 670px;
    background: var(--paper);
    overflow: hidden;
  }
  .page--front { left: 66px; }
  .page--inside { left: 619px; }
  .masthead {
    position: absolute;
    left: 0; top: 0;
    width: 100%;
    height: 70px;
    background: var(--brand-red);
  }
  .web-link {
    position: absolute;
    left: 353px;
    top: 26px;
    display: flex;
    align-items: center;
    gap: 7px;
    font-family: "Roboto Condensed", "Arial Narrow", sans-serif;
    font-weight: 700;
    font-size: 12px;
    color: var(--label-white);
  }
  .web-link svg { width: 18px; height: 18px; }
  .brand {
    position: absolute;
    left: 14px;
    top: 13px;
    width: 92px;
    display: flex;
    flex-direction: column;
    align-items: center;
    z-index: 2;
  }
  .brand-dot {
    width: 72px;
    height: 72px;
    border-radius: 50%;
    background: var(--mark-gold);
  }
  .brand-name {
    margin-top: 3px;
    font-family: "Montserrat", Arial, sans-serif;
    font-weight: 700;
    font-size: 12.5px;
    letter-spacing: 0.6px;
    color: var(--name-ink);
  }
  .hero-photo {
    position: absolute;
    left: 0; top: 70px;
    width: 100%;
    height: 235px;
    background: linear-gradient(135deg, #e6eef2 0%, #a9bcc8 35%, #5f7384 60%, #c7d5dd 85%, #eef3f5 100%);
  }
  .lead-title {
    position: absolute;
    left: 48px;
    top: 328px;
    font-weight: 600;
    font-size: 14.5px;
    color: var(--heading-ink);
  }
  .copy p {
    font-size: 9.4px;
    line-height: 14.1px;
    margin-bottom: 12px;
  }
  .lead-copy {
    position: absolute;
    left: 48px;
    top: 355px;
    width: 416px;
  }
  .columns {
    position: absolute;
    left: 48px;
    display: flex;
    gap: 21px;
  }
  .columns .column { width: 202px; }
  .page--front .columns { top: 486px; }
  .page--inside .columns { top: 133px; }
  .footer-band {
    position: absolute;
    left: 0; bottom: 0;
    width: 100%;
    height: 18px;
    background: var(--footer-band);
  }
</style>
</head>
<body>
  <div class="sheet-label">Newsletter_Template</div>

  <section class="page page--front">
    <header class="masthead">
      <div class="web-link">
        <svg viewBox="0 0 20 20" aria-hidden="true" fill="none" stroke="#fff" stroke-width="1.3">
          <circle cx="10" cy="10" r="8.5"/>
          <ellipse cx="10" cy="10" rx="4" ry="8.5"/>
          <line x1="1.5" y1="10" x2="18.5" y2="10"/>
          <line x1="3" y1="5.5" x2="17" y2="5.5"/>
          <line x1="3" y1="14.5" x2="17" y2="14.5"/>
        </svg>
        <span>https://orbalqa.example</span>
      </div>
    </header>
    <div class="brand">
      <div class="brand-dot"></div>
      <div class="brand-name">ORBALQa</div>
    </div>
    <div class="hero-photo" role="img" aria-label="Photo of business people walking through a bright glass-walled office atrium"></div>
    <h2 class="lead-title">Lorem ipsum dolor sit amet</h2>
    <div class="copy lead-copy">
      <p>Lorem ipsum dolor sit amet, consectetur adipiscing elit. Duis auctor sem vel metus interdum porta. Duis consequat bibendum felis eget cursus. Nulla eget purus vehicula ipsum finibus egestas. Nullam ligula ipsum, mollis sed gravida vitae, maximus eu dolor. Morbi luctus sem a congue consectetur.Orci varius natoque penatibus et magnis dis parturient montes, nascetur ridiculus mus. Vestibulum congue eros auctor, ullamcorper libero blandit, tempor tellus. Proin vitae tellus et nunc fringilla lacinia. Sed augue erat, facilisis laoreet velit a, convallis mattis nunc. Nunc sagittis ligula vitae sollicitudin sollicitudin.</p>
    </div>
    <div class="copy columns">
      <div class="column">
        <p>Lorem ipsum dolor sit amet, consectetur adipiscing elit. Duis auctor sem vel metus interdum porta. Duis consequat bibendum felis eget cursus. Nulla eget purus vehicula ipsum finibus egestas. Nullam ligula ipsum, mollis sed gravida vitae, maximus eu dolor. Morbi luctus sem a congue consectetur. Orci varius natoque penatibus et magnis dis parturient montes, nascetur ridiculus mus.</p>
      </div>
      <div class="column">
        <p>Vestibulum congue eros auctor, ullamcorper libero blandit, tempor tellus. Proin vitae tellus et nunc fringilla lacinia. Sed augue erat, facilisis laoreet velit a, convallis mattis nunc. Nunc sagittis ligula vitae sollicitudin sollicitudin. Orci varius natoque penatibus et magnis dis parturient montes, nascetur ridiculus mus. Vestibulum congue eros auctor, ullamcorper libero blandit, tempor tellus.</p>
      </div>
    </div>
    <div class="footer-band"></div>
  </section>

  <section class="page page--inside">
    <header class="masthead">
      <div class="web-link">
        <svg viewBox="0 0 20 20" aria-hidden="true" fill="none" stroke="#fff" stroke-width="1.3">
          <circle cx="10" cy="10" r="8.5"/>
          <ellipse cx="10" cy="10" rx="4" ry="8.5"/>
          <line x1="1.5" y1="10" x2="18.5" y2="10"/>
          <line x1="3" y1="5.5" x2="17" y2="5.5"/>
          <line x1="3" y1="14.5" x2="17" y2="14.5"/>
        </svg>
        <span>https://orbalqa.example</span>
      </div>
    </header>
    <div class="brand">
      <div class="brand-dot"></div>
      <div class="brand-name">ORBALQa</div>
    </div>
    <div class="copy columns">
      <div class="column">
        <p>Lorem ipsum dolor sit amet, consectetur adipiscing elit. Duis auctor sem vel metus interdum porta. Duis consequat bibendum felis eget cursus. Nulla eget purus vehicula ipsum finibus egestas. Nullam ligula ipsum, mollis sed gravida vitae, maximus eu dolor. Morbi luctus sem a congue consectetur.</p>
        <p>Orci varius natoque penatibus et magnis dis parturient montes, nascetur ridiculus mus. Vestibulum congue eros auctor, ullamcorper libero blandit, tempor tellus. Proin vitae tellus et nunc fringilla lacinia. Sed augue erat, facilisis laoreet velit a, convallis mattis nunc. Nunc sagittis ligula vitae sollicitudin sollicitudin. Orci varius natoque penatibus et magnis dis parturient montes, nascetur ridiculus mus.</p>
        <p>Vestibulum congue eros auctor, ullamcorper libero blandit, tempor tellus. Proin vitae tellus et nunc fringilla lacinia. Sed augue erat, facilisis laoreet velit a, convallis mattis nunc. Nunc sagittis ligula vitae sollicitudin sollicitudin.</p>
        <p>Nulla facilisi. Nulla quis odio vitae purus aliquam fermentum ut nec diam. Fusce sed velit ultrices, aliquam augue ut, sollicitudin orci. Orci varius natoque penatibus et magnis dis parturient montes, nascetur ridiculus mus. Vestibulum congue eros auctor, ullamcorper libero blandit, tempor tellus.</p>
      </div>
      <div class="column">
        <p>Proin vitae tellus et nunc fringilla lacinia. Sed augue erat, facilisis laoreet velit a, convallis mattis nunc. Nunc sagittis ligula vitae sollicitudin sollicitudin.</p>
        <p>Orci varius natoque penatibus et magnis dis parturient montes, nascetur ridiculus mus. Vestibulum congue eros auctor, ullamcorper libero blandit, tempor tellus. Proin vitae tellus et nunc fringilla lacinia. Sed augue erat, facilisis laoreet velit a, convallis mattis nunc. Nunc sagittis ligula vitae sollicitudin sollicitudin. Orci varius natoque penatibus et magnis dis parturient montes, nascetur ridiculus mus.</p>
        <p>Vestibulum congue eros auctor, ullamcorper libero blandit, tempor tellus. Proin vitae tellus et nunc fringilla lacinia. Sed augue erat, facilisis laoreet velit a, convallis mattis nunc. Nunc sagittis ligula vitae sollicitudin sollicitudin.</p>
        <p>Orci varius natoque penatibus et magnis dis parturient montes, nascetur ridiculus mus. Vestibulum congue eros auctor, ullamcorper libero blandit, tempor tellus. Proin vitae tellus et nunc fringilla lacinia. Sed augue erat, facilisis laoreet velit a, convallis mattis nunc. Nunc sagittis ligula vitae sollicitudin sollicitudin. Orci varius natoque penatibus et magnis dis parturient montes, nascetur ridiculus mus. Vestibulum congue eros auctor, ullamcorper libero blandit, tempor tellus.</p>
      </div>
    </div>
    <div class="footer-band"></div>
  </section>
</body>
</html>
```